Business Cards for Corvantis LLC

We need business cards for a new company called “Corvantis LLC”. This is a technology process improvement company providing a comprehensive assessment of the technology used to run their business. The documentation and review process delivers the visibility and reassurance they need to protect their business and plan for the future. The product is called “Halvorne Ledgerwork”. Our primary target is small-medium size businesses, with the deliverables going to the decision maker. We would like to see the designs use the color blue. Our tag line is PROTECT YOUR BUSINESS · TAKE CONTROL OF IT.

Industry/Entity Type

Business

Contact Information for Business Card

Tag line should be on back of card - it does not have to be upper case.

Requirements
Must have
• Please use information when laying out card:
• Name: Darnell Pruitt
• Title: Partner
• Phone Number: (877)555-0143
• Email: dell@corvantisllc.com
• Website: http://corvantisllc.com

```html
<!DOCTYPE html>
<html lang="en">
<head>
<meta charset="utf-8">
<title>Corvantis LLC — Business Cards</title>
<link rel="stylesheet" href="https://fonts.googleapis.com/css2?family=Open+Sans:ital,wght@0,400;0,600;1,400&display=swap">
<style>
  :root {
    --bg: #2c2c2e;
    --brand-blue: #1575c2;
    --brand-blue-dark: #0f5f9f;
    --paper: #ffffff;
    --ink-grey: #8a8f96;
    --ink-dark: #4a4f55;
  }
  * { box-sizing: border-box; margin: 0; padding: 0; }
  html, body {
    width: 1200px; height: 950px; overflow: hidden;
    background: var(--bg);
    font-family: "Open Sans", Arial, sans-serif;
  }
  .sheet {
    width: 1200px; height: 950px;
    display: flex; flex-direction: column;
    align-items: center; justify-content: center; gap: 60px;
  }
  .card {
    width: 630px; height: 360px;
    position: relative;
    border-radius: 4px;
    overflow: hidden;
  }
  /* Front */
  .card--front { background: var(--paper); }
  .brand {
    display: flex; align-items: center; gap: 12px;
    font-weight: 600; color: var(--brand-blue);
  }
  .brand__square { width: 20px; height: 20px; background: currentColor; }
  .card--front .brand {
    position: absolute; top: 62px; right: 56px;
    font-size: 36px; letter-spacing: 1px;
  }
  .divider {
    position: absolute; left: 56px; right: 56px; top: 168px;
    height: 1px; background: var(--brand-blue);
  }
  .person { position: absolute; left: 56px; top: 196px; }
  .person__name { font-size: 24px; font-weight: 600; color: var(--brand-blue); }
  .person__title { font-size: 15px; color: var(--ink-grey); margin-top: 2px; }
  .contact { list-style: none; margin-top: 20px; }
  .contact__item {
    display: flex; align-items: center; gap: 10px;
    font-size: 15px; color: var(--ink-dark); margin-top: 6px;
  }
  .contact__item svg { width: 14px; height: 14px; fill: var(--brand-blue-dark); }
  .website {
    position: absolute; right: 56px; top: 196px;
    font-size: 17px; font-weight: 600; color: var(--brand-blue);
    letter-spacing: 0.5px;
  }
  /* Back */
  .card--back {
    background: var(--brand-blue);
    display: flex; flex-direction: column; align-items: center; justify-content: center;
  }
  .card--back .brand { color: var(--paper); font-size: 44px; letter-spacing: 1px; }
  .card--back .brand__square { width: 26px; height: 26px; }
  .tagline {
    margin-top: 40px; color: var(--paper);
    font-style: italic; font-size: 17px;
  }
</style>
</head>
<body>
<main class="sheet">
  <section class="card card--front" aria-label="Card front">
    <div class="brand"><span class="brand__square"></span><span>Corvantis LLC</span></div>
    <div class="divider"></div>
    <div class="person">
      <p class="person__name">Darnell Pruitt</p>
      <p class="person__title">Partner</p>
      <ul class="contact">
        <li class="contact__item">
          <svg viewBox="0 0 24 24" aria-hidden="true"><path d="M6.6 10.8a15.1 15.1 0 0 0 6.6 6.6l2.2-2.2a1 1 0 0 1 1-.25 11.4 11.4 0 0 0 3.6.57 1 1 0 0 1 1 1V20a1 1 0 0 1-1 1A17 17 0 0 1 3 4a1 1 0 0 1 1-1h3.5a1 1 0 0 1 1 1c0 1.25.2 2.45.57 3.57a1 1 0 0 1-.25 1z"/></svg>
          (877)555-0143
        </li>
        <li class="contact__item">
          <svg viewBox="0 0 24 24" aria-hidden="true"><path d="M2 5h20v14H2zm2 2v.5l8 5 8-5V7z"/></svg>
          dell@corvantisllc.com
        </li>
      </ul>
    </div>
    <p class="website">www.corvantisllc.com</p>
  </section>

  <section class="card card--back" aria-label="Card back">
    <div class="brand"><span class="brand__square"></span><span>Corvantis LLC</span></div>
    <p class="tagline">Protect your business. Take control of it.</p>
  </section>
</main>
</body>
</html>
```